Mini Book (4.25 x 6) Cover Design for Christian authors

We need a book cover designed for a mini book (4.25 x 6). We will need a front, back and spine for the book.
The book is titled:
Tender Lantern
Subtitle:
Quiet Echoes Along Your Path
Authors:
Walter and Joanna Brightmoor
We are wanting the colors Dark Blue and Grey with more blue than grey.
We do not want any stock images or photos, only original work.
The cover should convey sincerity, intuition and truth with prestige.
We want the back cover text to be included (top) and the bios to be on the back as well (bottom). *Those documents are included in the files.
Since it is a mini book, it is important for the design to be simple and not cluttered, but powerful!
This is the first book in a twelve book series, so we would like the same "look" to carry through all twelve books, eventually.
On the back of the book, at the bottom (left), we want the following contact information:
Morning Harvest Method Logo (in files below)
willowgatehaven@mailbrook.net
555.318.2046
P.O.Box 871
Sedalia, CO 80199

Please save room on the back (bottom-right) for the ISBN and price.
Updates

Thank you to the designers that have submitted feedback concerning our design brief. We have made some changes that will perhaps make it easier to submit a variety of designs.Thank you! Added Saturday, March 4, 2017

Target Market(s)

Christians - mainly women

Industry/Entity Type

Religious

Font styles to use
Serif
Sans Serif
Decorative
Script
Other font styles liked:
• Not any particular font, looking for one that goes well with the cover design.

Requirements
Must have
• Mini Book Size (4.25 x 6)-spine size 1/8" (0.125)
• Dark blue and grey colors
• Cover needs to be simple and not cluttered or busy.
• Intriguing
• A font that is attractive, but it is still easy to read.
• *File information below
Nice to have
• Designs that are different from the mainstream.
• Perhaps a design that would do something different with the title/font? Maybe a repeat of the words from smaller to larger? Not sure how it would look, but maybe?
Should not have
• Any other colors but dark blue and grey
• Cluttered Look

```html
<!DOCTYPE html>
<html lang="en">
<head>
<meta charset="UTF-8">
<title>Tender Lantern — Cover Spread</title>
<link rel="stylesheet" href="https://fonts.googleapis.com/css2?family=Noto+Serif:ital,wght@0,400;0,700;1,400&display=swap">
<style>
  :root {
    --cover-blue: #2f3190;
    --cover-blue-deep: #262878;
    --spine-grey: #a8a8ab;
    --ink-white: #ffffff;
    --ink-soft: #e4e4ee;
    --ink-navy: #23256f;
    --page-bg: #ecebe8;
  }
  * { box-sizing: border-box; margin: 0; padding: 0; }
  html, body { width: 1200px; height: 800px; overflow: hidden; }
  body {
    background: var(--page-bg);
    font-family: "Noto Serif", Georgia, serif;
    display: flex; align-items: center; justify-content: center;
  }
  .cover-spread { display: flex; height: 720px; box-shadow: 0 6px 24px rgba(0,0,0,.18); }
  .panel { width: 504px; height: 720px; background: var(--cover-blue); color: var(--ink-white); position: relative; }

  /* Back cover */
  .back-cover { padding: 64px 44px 40px 52px; }
  .back-cover p, .back-cover li { font-size: 14.5px; line-height: 1.32; text-align: justify; }
  .author-intro { text-indent: 18px; font-weight: 700; }
  .process-blurb { margin-top: 48px; text-indent: 18px; font-weight: 700; }
  .book-promises { list-style: none; font-weight: 700; }
  .book-promises li { text-align: left; }
  .book-promises li::before { content: "\2022\00a0"; }
  .scripture { margin-top: 58px; font-style: italic; color: var(--ink-soft); font-size: 14px !important; }
  .contact-block { position: absolute; left: 52px; bottom: 46px; }
  .method-mark { display: flex; align-items: center; gap: 10px; margin-bottom: 16px; }
  .method-mark .dot { width: 44px; height: 44px; border-radius: 50%; background: var(--ink-white); }
  .method-mark span { font-size: 14px; font-weight: 700; }
  .contact-block address { font-style: normal; font-size: 13.5px; line-height: 1.3; }

  /* Spine */
  .spine {
    width: 40px; height: 720px; background: var(--spine-grey);
    display: flex; align-items: center; justify-content: center;
  }
  .spine-title {
    writing-mode: vertical-rl; color: var(--ink-navy);
    font-size: 20px; font-weight: 700; white-space: nowrap; letter-spacing: .5px;
  }

  /* Front cover */
  .front-cover { text-align: center; padding-top: 70px; }
  .book-title { font-size: 56px; font-weight: 700; line-height: 1.1; }
  .book-subtitle { font-size: 19px; font-weight: 700; margin-top: 26px; }
  .cover-art {
    display: block; width: 230px; height: 350px; margin: 70px auto 0;
  }
  .author-names { position: absolute; left: 0; right: 0; bottom: 70px; font-size: 21px; font-weight: 700; }
</style>
</head>
<body>
  <main class="cover-spread">
    <section class="panel back-cover">
      <p class="author-intro">International award winning authors, Joanna and Walter Brightmoor inspire couples and individuals to connect to the heart of God through Morning Harvest Method®. For over twenty years, they have conducted workshops and seminars throughout the country and at their private retreat center located in the Colorado mountains.</p>
      <p class="process-blurb">Morning Harvest Method (MHM)® proceeds, prepares and propels us into our Divine Inheritance. God always has our best interest at heart. By understanding His power, we are able to significantly impact the lives of others, leaving our imprint upon their hearts. This book will:</p>
      <ul class="book-promises">
        <li>Uncover the secret that is God’s plan</li>
        <li>Unveil God’s Six Significant Shields</li>
        <li>Unmask God’s Positioning Strategy (GPS)</li>
      </ul>
      <p class="scripture">“Come, let us go up to the mountain of the LORD, To the house (temple) of the God of Jacob; That He may teach us His ways And that we may walk in His paths.” ~ Isaiah 2:3</p>
      <div class="contact-block">
        <div class="method-mark"><div class="dot"></div><span>Morning Harvest Method</span></div>
        <address>
          willowgatehaven@mailbrook.net<br>
          P.O.Box 871 Sedalia, CO 80199<br>
          555.318.2046
        </address>
      </div>
    </section>

    <aside class="spine">
      <span class="spine-title">Tender Lantern: Quiet Echoes Along Your Path</span>
    </aside>

    <section class="panel front-cover">
      <h1 class="book-title">Tender Lantern</h1>
      <p class="book-subtitle">Quiet Echoes Along Your Path</p>
      <svg class="cover-art" viewBox="0 0 230 350" role="img" aria-label="White line-art fingerprint emblem">
        <defs>
          <radialGradient id="artGlow" cx="50%" cy="45%" r="60%">
            <stop offset="0%" stop-color="#5a5cb0"/>
            <stop offset="100%" stop-color="#2f3190"/>
          </radialGradient>
        </defs>
        <ellipse cx="115" cy="175" rx="112" ry="172" fill="url(#artGlow)"/>
      </svg>
      <p class="author-names">Walter and Joanna Brightmoor</p>
    </section>
  </main>
</body>
</html>
```